Advert for Services that we offer

Bolt Remova Ltd need an design to represent what we do in a modern way by showing an image with a brief description and the use of corporate logo the information we will proved vie a doc file and this is to be presented in a modern way. This design will be for print & web. we have done our own design and its not great i have put this in the file repository

Target Market(s)

Motor trade

Font styles to use
Sans Serif

Colors

Designer to choose colors to be used in the design.

Requirements
Must have
• Company colour scheme as per logo within the files uploaded.
• and a small boarder to isolate it from the rest of the articles.
Nice to have
• Modern font
Should not have
• Old style font

```html
<!DOCTYPE html>
<html lang="en">
<head>
<meta charset="utf-8">
<title>Bolt Remova Ltd – Product Testing &amp; Analysis</title>
<link rel="stylesheet" href="https://fonts.googleapis.com/css2?family=Open+Sans:wght@400;700&display=swap">
<style>
  :root {
    --brand-blue: #2474b9;
    --swoosh-grey: #b1b1b3;
    --ring-grey: #d6d6d6;
    --paper: #ffffff;
    --ink: #1a1a1a;
    --backdrop: #ffffff;
  }
  * { margin: 0; padding: 0; box-sizing: border-box; }
  html, body {
    width: 1200px; height: 831px; overflow: hidden;
    background: var(--backdrop);
    font-family: "Open Sans", Arial, sans-serif;
  }
  .advert {
    position: relative; width: 1200px; height: 831px;
    background: var(--brand-blue);
  }
  .advert__shapes { position: absolute; inset: 0; }

  .brand {
    position: absolute; left: 48px; top: 120px; width: 350px;
    display: flex; align-items: center; justify-content: center; gap: 12px;
  }
  .brand__mark { width: 26px; height: 26px; background: var(--brand-blue); }
  .brand__name {
    font-weight: 700; font-size: 34px; color: var(--brand-blue);
    letter-spacing: 0.5px; white-space: nowrap;
  }

  .services { position: absolute; left: 54px; top: 316px; list-style: none; }
  .services__item {
    display: flex; align-items: center; gap: 9px;
    height: 40px; margin-bottom: 35.5px;
  }
  .services__item:last-child { height: 56px; }
  .services__tick { width: 38px; height: 38px; flex: none; }
  .services__label {
    font-weight: 700; font-size: 25px; line-height: 22px;
    color: var(--brand-blue); letter-spacing: -0.6px; text-transform: uppercase;
  }

  .headline {
    position: absolute; left: 560px; top: 484px; width: 610px;
    text-align: center; color: var(--paper);
    font-weight: 700; font-size: 58px; line-height: 86px; letter-spacing: -0.5px;
  }

  .contact {
    position: absolute; top: 738px; height: 50px;
    display: flex; align-items: center; gap: 16px;
    color: var(--ink); font-size: 25px; letter-spacing: 0.6px;
  }
  .contact--phone { left: 168px; }
  .contact--web { left: 594px; }
  .contact__icon { width: 44px; height: 44px; }
</style>
</head>
<body>
<main class="advert">
  <svg class="advert__shapes" viewBox="0 0 1200 831" width="1200" height="831">
    <defs>
      <clipPath id="panel-clip"><rect x="20" y="20" width="1160" height="790"/></clipPath>
      <clipPath id="photo-clip"><circle cx="900" cy="250" r="370"/></clipPath>
      <linearGradient id="photo-tones" x1="0" y1="0" x2="1" y2="1">
        <stop offset="0" stop-color="#c9c6c2"/>
        <stop offset="0.45" stop-color="#9a928c"/>
        <stop offset="0.7" stop-color="#8a4a34"/>
        <stop offset="1" stop-color="#3b3f46"/>
      </linearGradient>
    </defs>
    <rect class="panel" x="20" y="20" width="1160" height="790" fill="var(--paper)"/>
    <g clip-path="url(#panel-clip)">
      <circle class="photo-ring" cx="900" cy="250" r="393" fill="var(--ring-grey)"/>
      <g role="img" aria-label="Photo of a technician measuring the bore of a red-painted flanged housing with a dial gauge in a workshop">
        <rect x="500" y="0" width="700" height="640" fill="url(#photo-tones)" clip-path="url(#photo-clip)"/>
      </g>
      <path class="swoosh" d="M20,262 C300,280 560,170 690,20 L730,20 C600,200 330,292 20,280 Z" fill="var(--swoosh-grey)"/>
      <path class="blue-wave" d="M405,719 C440,600 520,520 601,486 C700,440 800,425 910,426 C1020,427 1110,432 1180,440 L1180,719 Z" fill="var(--brand-blue)"/>
      <rect class="footer-strip" x="20" y="719" width="1160" height="91" fill="var(--paper)"/>
    </g>
  </svg>

  <div class="brand">
    <span class="brand__mark"></span>
    <span class="brand__name">BOLT REMOVA LTD</span>
  </div>

  <ul class="services">
    <li class="services__item">
      <svg class="services__tick" viewBox="0 0 38 38"><circle cx="19" cy="19" r="19" fill="var(--brand-blue)"/><circle cx="19" cy="19" r="14" fill="none" stroke="#fff" stroke-width="2"/><polyline points="12,19 17,24 26,14" fill="none" stroke="#fff" stroke-width="4" stroke-linecap="round" stroke-linejoin="round"/></svg>
      <span class="services__label">Metallurgical Testing</span>
    </li>
    <li class="services__item">
      <svg class="services__tick" viewBox="0 0 38 38"><circle cx="19" cy="19" r="19" fill="var(--brand-blue)"/><circle cx="19" cy="19" r="14" fill="none" stroke="#fff" stroke-width="2"/><polyline points="12,19 17,24 26,14" fill="none" stroke="#fff" stroke-width="4" stroke-linecap="round" stroke-linejoin="round"/></svg>
      <span class="services__label">Bearing Pre-Load Testing</span>
    </li>
    <li class="services__item">
      <svg class="services__tick" viewBox="0 0 38 38"><circle cx="19" cy="19" r="19" fill="var(--brand-blue)"/><circle cx="19" cy="19" r="14" fill="none" stroke="#fff" stroke-width="2"/><polyline points="12,19 17,24 26,14" fill="none" stroke="#fff" stroke-width="4" stroke-linecap="round" stroke-linejoin="round"/></svg>
      <span class="services__label">Bore Measurement</span>
    </li>
    <li class="services__item">
      <svg class="services__tick" viewBox="0 0 38 38"><circle cx="19" cy="19" r="19" fill="var(--brand-blue)"/><circle cx="19" cy="19" r="14" fill="none" stroke="#fff" stroke-width="2"/><polyline points="12,19 17,24 26,14" fill="none" stroke="#fff" stroke-width="4" stroke-linecap="round" stroke-linejoin="round"/></svg>
      <span class="services__label">New Product Evaluation</span>
    </li>
    <li class="services__item">
      <svg class="services__tick" viewBox="0 0 38 38"><circle cx="19" cy="19" r="19" fill="var(--brand-blue)"/><circle cx="19" cy="19" r="14" fill="none" stroke="#fff" stroke-width="2"/><polyline points="12,19 17,24 26,14" fill="none" stroke="#fff" stroke-width="4" stroke-linecap="round" stroke-linejoin="round"/></svg>
      <span class="services__label">Product Analysis &amp;<br>Report</span>
    </li>
  </ul>

  <h1 class="headline">PRODUCT&nbsp;&nbsp;TESTING<br>&amp; ANALYSIS</h1>

  <div class="contact contact--phone">
    <svg class="contact__icon" viewBox="0 0 44 44"><path d="M9,3 C6,4 3,8 4,13 C7,25 17,36 30,41 C35,42 39,39 41,36 L35,29 C33,28 31,29 30,31 L28,32 C22,29 16,22 13,16 L15,14 C17,13 17,11 16,9 Z" fill="var(--brand-blue)"/></svg>
    <span class="contact__text">0161 555 0192</span>
  </div>
  <div class="contact contact--web">
    <svg class="contact__icon" viewBox="0 0 44 44" fill="none" stroke="var(--brand-blue)" stroke-width="3"><circle cx="22" cy="22" r="19"/><ellipse cx="22" cy="22" rx="8" ry="19"/><line x1="22" y1="3" x2="22" y2="41"/><line x1="3" y1="22" x2="41" y2="22"/><path d="M6,12 H38 M6,32 H38"/></svg>
    <span class="contact__text">WWW.BOLT-REMOVA.CO.UK</span>
  </div>
</main>
</body>
</html>
```